High end boutique food product label

We are looking for a label design to be used on our range of high end food products. We don't have a design or colour scheme in mind and are interested to see what ideas are submitted.
We would like it to feel sophisticated, chic, and eye-catching.
All of our products are handmade in Australia using Australian ingredients.
The graphics for the label will need to be scaleable to be fit a variety of labels from small squat jars with labels sized 3.5cm high and 7cm wide, to tall thin bottles with labels that are 14cm high and 4.5cm wide.
We would be interested in working with the winning designer to create these different sized labels.
The label submitted for this project should be 14cm high and 4.5cm wide, it should include our logo (file supplied in .jpeg and .ai), the product name 'Extra Virgin Olive Oil' and the size '250ml'.
This is just the front label on a bottle, we are not expecting a rear label to be created currently.
You are welcome to use any fonts you think will look good but the fonts used in our logo are Allaina Medium and Bebas Kai Regular.

```html
<!DOCTYPE html>
<html lang="en">
<head>
<meta charset="UTF-8">
<title>Hearth &amp; Vale — Extra Virgin Olive Oil Label</title>
<link rel="stylesheet" href="https://fonts.googleapis.com/css2?family=Playfair+Display:wght@400;700&family=Oswald:wght@300;500&display=swap">
<style>
  :root {
    --page: #ffffff;
    --label-top: #3e2d21;
    --label-mid: #5d4a39;
    --label-low: #7d6b55;
    --label-bottom: #a08f71;
    --cream: #f4efe6;
    --gold: #e0ac3f;
    --ink: #3a3026;
    --scene-a: #6f5e4a;
    --scene-b: #8a785f;
  }
  * { margin: 0; padding: 0; box-sizing: border-box; }
  html, body {
    width: 1200px;
    height: 1200px;
    overflow: hidden;
    background: var(--page);
  }
  .canvas {
    position: relative;
    width: 1200px;
    height: 1200px;
  }
  .label {
    position: absolute;
    left: 435px;
    top: 80px;
    width: 330px;
    height: 1040px;
    background: linear-gradient(180deg,
      var(--label-top) 0%,
      var(--label-mid) 35%,
      var(--label-low) 65%,
      var(--label-bottom) 100%);
    text-align: center;
  }
  .brand-name {
    position: absolute;
    top: 150px;
    left: 0;
    width: 100%;
    font-family: "Playfair Display", serif;
    font-weight: 700;
    font-size: 38px;
    line-height: 1;
    color: var(--cream);
  }
  .product-type {
    position: absolute;
    top: 418px;
    left: 0;
    width: 100%;
    font-family: "Playfair Display", serif;
    font-weight: 400;
    font-size: 31px;
    color: var(--gold);
  }
  .product-name {
    position: absolute;
    top: 466px;
    left: 0;
    width: 100%;
    font-family: "Playfair Display", serif;
    font-weight: 700;
    font-size: 48px;
    color: var(--cream);
  }
  .landscape-art {
    position: absolute;
    top: 600px;
    left: 0;
    width: 100%;
    height: 258px;
    display: block;
  }
  .origin-note {
    position: absolute;
    top: 884px;
    left: 0;
    width: 100%;
    font-family: "Oswald", sans-serif;
    font-weight: 300;
    font-size: 18px;
    line-height: 29px;
    letter-spacing: 1.2px;
    color: var(--ink);
  }
  .divider {
    position: absolute;
    top: 952px;
    left: 110px;
    width: 110px;
    height: 4px;
    background: var(--gold);
  }
  .volume {
    position: absolute;
    top: 972px;
    left: 0;
    width: 100%;
    font-family: "Oswald", sans-serif;
    font-weight: 500;
    font-size: 23px;
    letter-spacing: 2px;
    color: var(--ink);
  }
</style>
</head>
<body>
  <main class="canvas">
    <section class="label">
      <div class="brand-name">Hearth &amp; Vale</div>

      <div class="product-type">Extra Virgin</div>
      <div class="product-name">Olive Oil</div>

      <svg class="landscape-art" role="img" aria-label="Sketched illustration of a hillside farmhouse above rows of olive trees" viewBox="0 0 330 258" preserveAspectRatio="none">
        <defs>
          <linearGradient id="sceneTone" x1="0" y1="0" x2="0" y2="1">
            <stop offset="0" stop-color="var(--scene-a)" stop-opacity="0"/>
            <stop offset="0.3" stop-color="var(--scene-a)" stop-opacity="0.55"/>
            <stop offset="0.75" stop-color="var(--scene-b)" stop-opacity="0.55"/>
            <stop offset="1" stop-color="var(--scene-b)" stop-opacity="0"/>
          </linearGradient>
        </defs>
        <rect x="0" y="0" width="330" height="258" fill="url(#sceneTone)"/>
      </svg>

      <p class="origin-note">HANDMADE IN AUSTRALIA<br>WITH AUSTRALIAN INGREDIENTS</p>
      <div class="divider"></div>
      <div class="volume">250ML</div>
    </section>
  </main>
</body>
</html>
```